Lira Vantell Music Flyer for Social Media

The flyer needs to include the networks Lira Vantell music is distributed on such as TuneHarbor, WaveCastFM, Brook, and Soundly. This flyer will be posted on social media websites such as friendloop, Pictogrove, and Chirpnet. The flyer will also be listed on the music artist official website. The artist logo is attached for additional creative ideas.

Target Market(s)

Music lovers

Industry/Entity Type

Music Download

Requirements
Must have
• Must have the music networks listed on the photo and the artist name.
Nice to have
• It would be nice to have the website listed: www.liravantell.example and artist logo.
Should not have
• Anything that is not listed in the project description.

```html
<!DOCTYPE html>
<html lang="en">
<head>
<meta charset="utf-8">
<title>Lira Vantell – Music Flyer</title>
<link rel="stylesheet" href="https://fonts.googleapis.com/css2?family=Anton&family=Kaushan+Script&family=Oswald:wght@500;700&family=Open+Sans:wght@300;600;700&family=Cinzel&display=swap">
<style>
:root{
  --pink:#e8205f;
  --pink-light:#f06e91;
  --ink:#111111;
  --paper:#f1f0f0;
  --paper-dark:#d6d4d5;
  --silver:#c9c9cb;
  --silver-dark:#8a8a8d;
  --white:#ffffff;
}
*{margin:0;padding:0;box-sizing:border-box}
html,body{width:1200px;height:964px;overflow:hidden;background:var(--paper)}
.flyer{position:relative;width:1200px;height:964px;overflow:hidden;
  background:radial-gradient(ellipse at 30% 40%,#ffffff 0%,var(--paper) 45%,var(--paper-dark) 100%);
  font-family:"Open Sans",sans-serif;color:var(--ink)}
.brand-name{position:absolute;left:40px;top:72px;width:330px;text-align:center;font-family:"Open Sans",sans-serif;font-weight:600;font-size:40px;line-height:56px;color:var(--ink)}
.brand-caption{position:absolute;left:42px;top:192px;font-family:"Cinzel",serif;font-size:24px;line-height:32px;letter-spacing:13px;color:var(--ink);white-space:nowrap}
.artist-title{position:absolute;left:700px;top:18px;font-family:"Kaushan Script",cursive;font-weight:400;font-size:86px;line-height:120px;color:var(--pink);white-space:nowrap}
.networks{position:absolute;left:30px;top:390px;width:190px;list-style:none;z-index:2}
.networks li{display:flex;align-items:center;gap:8px;height:78px;font-family:"Open Sans",sans-serif;font-weight:700;font-size:24px;color:var(--ink);white-space:nowrap}
.networks .dot{flex:none;width:22px;height:22px;border-radius:50%;background:var(--ink)}
.photo-side{position:absolute;left:231px;top:293px;width:246px;height:407px;border-radius:50%;
  background:linear-gradient(160deg,#a0705c,#5a3a30 60%,#2a1d1c);border:5px solid var(--pink);
  box-shadow:0 0 0 4px var(--silver)}
.ring{position:absolute;left:429px;top:140px;width:590px;height:590px;border-radius:50%;
  background:linear-gradient(180deg,#f4f4f5 0%,var(--silver) 45%,#2a2a2a 52%,var(--silver-dark) 70%,#f4f4f5 100%);
  box-shadow:0 6px 18px rgba(0,0,0,.35)}
.photo-main{position:absolute;left:471px;top:182px;width:506px;height:506px;border-radius:50%;
  background:radial-gradient(circle at 45% 40%,#b27a62 0%,#6b4248 40%,#2d1d28 75%,#1c1318 100%)}
.role-badge{position:absolute;left:925px;top:162px;width:226px;height:226px;border-radius:50%;
  background:radial-gradient(circle at 40% 30%,var(--pink-light),var(--pink) 60%);
  box-shadow:0 4px 10px rgba(0,0,0,.3);display:flex;align-items:center;justify-content:center;text-align:center;
  font-family:"Oswald",sans-serif;font-weight:700;font-size:48px;line-height:50px;color:var(--white)}
.site-pill{position:absolute;left:767px;top:650px;width:393px;height:50px;border-radius:25px;background:var(--pink);
  display:flex;align-items:center;justify-content:center;font-family:"Oswald",sans-serif;font-weight:700;font-size:25px;letter-spacing:2px;color:var(--white);white-space:nowrap}
.ep-title{position:absolute;left:50px;top:728px;font-family:"Anton",sans-serif;font-weight:400;font-size:70px;line-height:80px;color:var(--ink);letter-spacing:4px;white-space:nowrap}
.socials{position:absolute;left:692px;top:746px;display:flex;gap:2px}
.socials li{list-style:none;width:60px;display:flex;flex-direction:column;align-items:center;gap:3px;font-size:10px;line-height:13px;font-weight:600;color:var(--ink);white-space:nowrap}
.socials .dot{width:46px;height:46px;border-radius:50%;background:var(--silver-dark)}
.info-band{position:absolute;left:0;top:817px;width:1200px;height:147px;background:var(--pink)}
.bio{position:absolute;left:42px;top:830px;width:895px;font-weight:300;font-size:18.5px;line-height:28.5px;color:var(--white)}
.release-badge{position:absolute;left:950px;top:725px;width:212px;height:212px;border-radius:50%;
  background:radial-gradient(circle at 45% 35%,#ffffff 55%,#d9d9d9 100%);box-shadow:0 3px 10px rgba(0,0,0,.35);
  display:flex;flex-direction:column;align-items:center;justify-content:center;text-align:center}
.release-badge .song{font-family:"Anton",sans-serif;font-size:40px;line-height:48px;color:var(--ink)}
.release-badge .meta{margin-top:6px;font-family:"Oswald",sans-serif;font-weight:500;font-size:18px;line-height:24px;color:#333}
</style>
</head>
<body>
<main class="flyer">
  <div class="brand-name">Lira Vantell</div>
  <div class="brand-caption">LIRA VANTELL</div>
  <h1 class="artist-title">Lira Vantell</h1>

  <div class="photo-side" role="img" aria-label="Full-length photo of the artist in black outfit against a brick wall"></div>
  <div class="ring"></div>
  <div class="photo-main" role="img" aria-label="Close-up portrait photo of the artist"></div>

  <ul class="networks">
    <li><span class="dot"></span>Brook</li>
    <li><span class="dot"></span>TuneHarbor</li>
    <li><span class="dot"></span>WaveCastFM</li>
    <li><span class="dot"></span>Soundly</li>
  </ul>

  <div class="role-badge">SINGER<br>&amp; SONG<br>WRITER</div>
  <div class="site-pill">www.liravantell.example</div>

  <h2 class="ep-title">VELVET PATIENCE EP</h2>
  <ul class="socials">
    <li><span class="dot"></span>friendloop</li>
    <li><span class="dot"></span>Chirpnet</li>
    <li><span class="dot"></span>Pictogrove</li>
    <li><span class="dot"></span>ViewStream</li>
  </ul>

  <div class="info-band"></div>
  <p class="bio">Marisol Dent born June 27, 1992 is an American singer and songwriter. Raised in Harlow Creek, SC she first entered the music industry by recording demo tapes in 2013. The independent artist released her EP "Velvet Patience" in 2016, and it is globally distributed worldwide. Lira Vantell graduated from Ridgeline Central High School, and she is currently attending Eastvale State University to further her education.</p>

  <div class="release-badge">
    <div class="song">DRIFT<br>TOGETHER</div>
    <div class="meta">by Lira Vantell:<br>Released 2016</div>
  </div>
</main>
</body>
</html>
```